Text heavy poster for university audience

I have developed a set of standards for online teaching that need to be turned into a post format. The project has a logo which should be incorporated. Most of the designing will be in terms of text layout. The logo (two versions - higher quality files available) and the a sample of standards (as image - word version available; the example is one third of standards) are attached. Design that can be adapted to brochure format would be great. (Brochure adaption will be paid separately via another project to be opened here). More details available here: http://www.brivelquarto.net
Updates

Dear all,

The URL for the site needs to be include in the design - either as footer or under logo:
<http://www.brivelquarto.net>

Sorry for late notice

Target Market(s)

The are university staff

Industry/Entity Type

University

Font styles to use
Serif
Sans Serif

Requirements
Must have
• The text in the "required" attachment must be included; but for initial draft feel free to restrict your design to "sample" attachment
The green from the Logo (PANTONE 17-5641 Emerald) should be the foundation of the colour palette.
Nice to have
• The collaborators as named here: http://www.brivelquarto.net/collaborators/
My preferred find is helvetica neue, but similar can be used
Should not have
• Decorative fonts

```html
<!DOCTYPE html>
<html lang="en">
<head>
<meta charset="utf-8">
<title>Brivel Quarto Standards – Online Education Poster</title>
<link href="https://fonts.googleapis.com/css2?family=Arimo:ital,wght@0,400;0,700;1,400;1,700&display=swap" rel="stylesheet">
<style>
:root{
  --emerald:#1e9a78;
  --emerald-light:#2fb58f;
  --ink-dark:#141414;
  --ink-mid:#2c2c2c;
  --panel:#3c3c3c;
  --panel-edge:#4a4a4a;
  --text-light:#e6e6e6;
  --text-soft:#b5b5b5;
  --text-dim:#8d8d8d;
  --swoosh:#9a9a9a;
  --page:#ffffff;
}
*{margin:0;padding:0;box-sizing:border-box}
html,body{width:1200px;height:1000px;overflow:hidden;background:var(--page)}
body{font-family:"Arimo",Arial,sans-serif;position:relative}
.poster{position:absolute;left:282px;top:25px;width:666px;height:943px;
  background:linear-gradient(180deg,var(--ink-dark) 0%,#1d1d1d 40%,var(--ink-mid) 70%,#1a1a1a 100%);overflow:hidden}
.poster-bands{position:absolute;left:0;top:0;width:666px;height:943px}
.brand{position:absolute;left:18px;top:12px;display:flex;align-items:center;gap:10px}
.brand-mark{width:50px;height:50px;background:var(--page)}
.brand-name{color:var(--page);font-weight:700;font-size:15px;line-height:17px;text-transform:uppercase;letter-spacing:.3px}
.site-url{position:absolute;right:14px;top:12px;color:var(--page);font-weight:700;font-size:21px;letter-spacing:2.2px}
.watermark-word{position:absolute;left:-203px;top:335px;width:476px;height:80px;transform:rotate(-90deg);
  font-weight:700;font-style:italic;font-size:76px;line-height:80px;letter-spacing:2px;color:#333;text-align:center}
.standards{position:absolute;left:78px;width:330px;color:var(--text-light)}
.section-title{color:var(--emerald-light);font-weight:700;font-size:12px;letter-spacing:.3px}
.section-intro{font-size:7px;line-height:9px;margin-bottom:6px}
.standard{margin-bottom:7px}
.standard h3{font-size:6.2px;font-weight:700;font-style:italic;text-transform:uppercase;line-height:8px;padding-left:6px;text-indent:-6px}
.standard ul{list-style:none;padding-left:12px}
.standard li{font-size:4.8px;line-height:6.4px;color:var(--text-soft)}
.standard li b{color:var(--text-light)}
.divider{position:absolute;left:78px;width:320px;height:1px;background:#555}
.collab-panel{position:absolute;left:415px;top:65px;width:253px;height:855px;border-radius:8px 0 0 8px;
  background:linear-gradient(90deg,var(--panel-edge),var(--panel) 20%,#353535)}
.collab-title{position:absolute;left:17px;top:6px;color:var(--emerald-light);font-weight:700;font-style:italic;font-size:11.5px}
.collab-rule{position:absolute;left:125px;top:28px;width:1px;height:812px;background:var(--swoosh)}
.collab-list{position:absolute;top:28px;list-style:none;width:115px}
.collab-list li{font-size:4.4px;line-height:9.2px;color:var(--text-dim);white-space:nowrap}
.collab-list.left{left:6px;text-align:right}
.collab-list.right{left:133px;text-align:left}
</style>
</head>
<body>
<main class="poster">
  <svg class="poster-bands" viewBox="0 0 666 943" aria-hidden="true">
    <path d="M0 0H666V62Q330 70 0 138Z" fill="var(--emerald)"/>
    <path d="M0 138Q330 70 666 62V72Q330 82 0 150Z" fill="var(--swoosh)" opacity=".8"/>
    <path d="M0 150Q330 82 666 72V76Q330 88 0 158Z" fill="#5a5a5a" opacity=".6"/>
    <path d="M0 925Q330 915 666 918V943H0Z" fill="var(--emerald)"/>
    <path d="M0 921Q330 911 666 914V918Q330 915 0 925Z" fill="var(--swoosh)"/>
  </svg>

  <header class="brand">
    <div class="brand-mark"></div>
    <div class="brand-name">Brivel<br>Quarto<br>Standards</div>
  </header>
  <div class="site-url">WWW.BRIVELQUARTO.NET</div>

  <div class="watermark-word">STANDARDS</div>

  <section class="standards" style="top:127px">
    <h2 class="section-title">ONE: STUDENTS</h2>
    <p class="section-intro">Students are supported in their online learning with a quality <b>curriculum</b> [1-4], opportunities for interaction with peers and staff [5&amp;6], and appropriate <b>support</b> [7&amp;8].</p>
    <div class="standard"><h3>1. Curriculum materials are aligned, available and engaging</h3><ul><li><b>Threshold</b> - The necessary materials are constructively aligned and available online</li><li><b>Good</b> - The materials are provided using a variety of media to engage students and support diversity</li><li><b>Excellent</b></li></ul></div>
    <div class="standard"><h3>2. Learning activities are aligned, available and engaging</h3><ul><li><b>Threshold</b> - Constructively aligned learning activities are available online</li><li><b>Good</b> - Learning activities use a variety of appropriate technologies to engage students and support diversity</li><li><b>Excellent</b></li></ul></div>
    <div class="standard"><h3>3. Assessment tasks are aligned, available and engaging</h3><ul><li><b>Threshold</b> - Constructively aligned assessment tasks are available online</li><li><b>Good</b> - Assessment tasks use a variety of appropriate technologies to engage students and support diversity</li><li><b>Excellent</b></li></ul></div>
    <div class="standard"><h3>4. Students are provided with timely, improvement focused formative feedback</h3><ul><li><b>Threshold</b> - Appropriate technologies are used to provide students with formative feedback in a timely manner</li><li><b>Good</b> - Feedback is provided in a variety of media to engage students and support diversity</li><li><b>Excellent</b></li></ul></div>
    <div class="standard"><h3>5. Students are provided with opportunities to interact with peers</h3><ul><li><b>Threshold</b> - There are opportunities for social interaction</li><li><b>Good</b> - There are opportunities for learning-focused interaction</li><li><b>Excellent</b></li></ul></div>
    <div class="standard"><h3>6. Students are provided with opportunities to interact with staff</h3><ul><li><b>Threshold</b> - Staff are provided with opportunities to answer student queries</li><li><b>Good</b> - Staff are provided with opportunities to be active participants in learning-focused interactions</li><li><b>Excellent</b></li></ul></div>
    <div class="standard"><h3>7. Students are provided with appropriate learning support</h3><ul><li><b>Threshold</b> - Appropriate, up-to-date and reliable learning guides and resources are provided online</li><li><b>Good</b> - A range of appropriate, up-to-date and reliable online learning skills workshops are available</li><li><b>Excellent</b></li></ul></div>
    <div class="standard"><h3>8. Students are supported in their use of educational technology</h3><ul><li><b>Threshold</b> - Appropriate, up-to-date and reliable technological guides and resources are provided online</li><li><b>Good</b> - Appropriate, timely and reliable asynchronous technological support is available</li><li><b>Excellent</b></li></ul></div>
  </section>

  <div class="divider" style="top:467px"></div>

  <section class="standards" style="top:476px">
    <h2 class="section-title">TWO: STAFF</h2>
    <p class="section-intro">Staff are supported in their online teaching with quality professional development [9], resourcing [10] and technical support [11].</p>
    <div class="standard"><h3>9. Staff are provided with quality professional development in online education</h3><ul><li><b>Threshold</b> - A range of appropriate, up-to-date and informative professional development activities are available to staff</li><li><b>Good</b> - The organisation requires staff to engage in continued professional development relevant to online education</li><li><b>Excellent</b></li></ul></div>
    <div class="standard"><h3>10. Online education is recognised in workload</h3><ul><li><b>Threshold</b> - Online teaching is recognised in workload</li><li><b>Good</b> - Online unit development is recognised in workload</li><li><b>Excellent</b></li></ul></div>
    <div class="standard"><h3>11. Staff are supported in their use of educational technology</h3><ul><li><b>Threshold</b> - Appropriate, up-to-date and reliable technological guides and resources are provided online</li><li><b>Good</b> - Appropriate, timely and reliable asynchronous technological support is available</li><li><b>Excellent</b></li></ul></div>
  </section>

  <div class="divider" style="top:631px"></div>

  <section class="standards" style="top:640px">
    <h2 class="section-title">THREE: ORGANISATION</h2>
    <p class="section-intro">The organisation supports online education through the provision of quality leadership [12-13], infrastructure [14] and evaluation [15-17]</p>
    <div class="standard"><h3>12. The organisation provides strategic leadership in online education</h3><ul><li><b>Threshold</b> - The organisation has a clearly articulated strategic position on online education</li><li><b>Good</b> - An appropriate member of the executive has explicit responsibility for online education</li><li><b>Excellent</b></li></ul></div>
    <div class="standard"><h3>13. The organisation employs a systematic approach to resource allocation in online education</h3><ul><li><b>Threshold</b> - There is a systematic approach to resource allocation</li><li><b>Good</b> - There is systematic approach with formal criteria that are widely available</li><li><b>Excellent</b></li></ul></div>
    <div class="standard"><h3>14. The organisation maintains and supports a quality learning platform for delivering online education</h3><ul><li><b>Threshold</b> - The organisation maintains and supports an appropriate learning platform</li><li><b>Good</b> - The learning platform provided is fit for purpose, scalable and reliable</li><li><b>Excellent</b></li></ul></div>
    <div class="standard"><h3>15. The organisation has a process for evaluating and improving student satisfaction with online education</h3><ul><li><b>Threshold</b> - The organisation has a systematic process for evaluating student satisfaction with online education</li><li><b>Good</b> - The organisation has a systematic process for improving student learning outcomes and satisfaction with online education and communicating improvements to students</li><li><b>Excellent</b></li></ul></div>
    <div class="standard"><h3>16. The organisation has a process for evaluating and improving training and support for staff</h3><ul><li><b>Threshold</b> - The organisation has a systematic process for evaluating and improving staff training and support</li><li><b>Good</b> - The organisation has a systematic process for improving staff training and support and communicating improvements to staff</li><li><b>Excellent</b></li></ul></div>
    <div class="standard"><h3>17. The organisation has a process for evaluating and improving infrastructure</h3><ul><li><b>Threshold</b> - The organisation has a systematic process for evaluating and improving infrastructure</li><li><b>Good</b> - The organisation has a systematic process for improving infrastructure and communicating improvements to stakeholders</li><li><b>Excellent</b></li></ul></div>
  </section>

  <aside class="collab-panel">
    <h2 class="collab-title">Dana Corwell and Collaborators</h2>
    <div class="collab-rule"></div>
    <ul class="collab-list left">
      <li>Abernath, Corin (Corrin Institute)</li><li>Ackery, Tamsin (Vellmore University)</li><li>Adlam, Verity (Wyndale University)</li><li>Aldwin, Pell (Kestrel Learning)</li><li>Allport, Noor (Harlow Bay)</li><li>Amberley, Keir (Tessaly)</li><li>Ansell, Rowan (Ravensmere University)</li><li>Arkwell, Juno (Tessaly)</li><li>Ashdown, Leni (Eastfold University)</li><li>Atherly, Brisa (Tessaly)</li><li>Aubrey-Lane, Otis (Ravensmere University)</li><li>Avenell, Sorrel (Corrin Institute)</li><li>Bagshaw, Ilse (Corrin Institute)</li><li>Balfry, Teodor (Harlow Bay)</li><li>Barrowman, Quill (Vellmore University)</li><li>Beckett-Hale, Mira (Tessaly)</li><li>Bellamont, Ezra (Tessaly)</li><li>Benwick, Talia (Harlow Bay)</li><li>Birchall, Fenn (Eastfold University)</li><li>Blakemore, Ysolde (Corrin Institute)</li><li>Bolton-Rye, Cass (Harlow Bay)</li><li>Bramley, Hollis (Vellmore University)</li><li>Brennick, Oona (Harlow Bay)</li><li>Brockway, Lyle (Harlow Bay)</li><li>Burcott, Wren (Harlow Bay)</li><li>Caddell, Pippa (Northgate University)</li><li>Calloway, Bram (Corrin Institute)</li><li>Carrow, Delphine (Vellmore University)</li><li>Castellan, Ivo (Corrin Institute)</li><li>Chalmer, Reeve (Corrin Institute)</li><li>Chesney, Alba (Ashcombe)</li><li>Claybourne, Nico (Harlow Bay)</li><li>Coldwell, Sabeen (Northgate University)</li><li>Corbin, Elric (Eastfold University)</li><li>Cottam, Marli (Corrin Institute)</li><li>Cresswell, Tobin (Eastfold University)</li><li>Culver, Ines (Northgate University)</li><li>Dalgety, Rafe (Harlow Bay)</li><li>Danvers, Lotte (Corrin Institute)</li><li>Daubney, Caius (Vellmore University)</li><li>Dellow, Yara (Ravensmere University)</li><li>Denholm, Aldo (Wyndale University)</li><li>Dorrington, Bex (Tessaly)</li><li>Drayton, Hal (Ashcombe)</li><li>Dunmore, Calla (Ravensmere University)</li><li>Eastwell, Jory (Harlow Bay)</li><li>Edgerly, Saffi (Pellbrook)</li><li>Elsworth, Marten (Harlow Bay)</li><li>Emmerton, Giulia (Eastfold University)</li><li>Farrant, Odell (Corrin Institute)</li><li>Fenwick-Holt, Avis (Ravensmere University)</li><li>Finchley, Roan (Ravensmere University)</li><li>Fordyce, Keziah (Northgate University)</li><li>Foxwell, Dov (Tessaly)</li><li>Galloway-Pike, Nell (Harlow Bay)</li><li>Garnock, Silas (Vellmore University)</li><li>Gifford, Thea (Corrin Institute)</li><li>Glenister, Arlo (Eastfold University)</li><li>Goodhew, Persis (Tessaly)</li><li>Gravell, Emrys (Eastfold University)</li><li>Greaves-Tan, Lior (Harlow Bay)</li><li>Hadley, Ottilie (Tessaly)</li><li>Halloran, Bastian (Northgate University)</li><li>Harcourt, Ngaio (Corrin Institute)</li><li>Hartigan, Lucan (Ravensmere University)</li><li>Haverly, Sunniva (Harlow Bay)</li><li>Hebden, Cato (Eastfold University)</li><li>Hensley, Marisol (Tessaly)</li><li>Hollis-Ward, Fitz (Vellmore University)</li><li>Hurrell, Anouk (Harlow Bay)</li><li>Ibbotson, Reza (Corrin Institute)</li><li>Ingleby, Clio (Northgate University)</li><li>Jarrold, Tamsen (Eastfold University)</li><li>Jessop, Aurel (Tessaly)</li><li>Kavanagh-Roe, Iris (Ravensmere University)</li><li>Kellaway, Dorian (Harlow Bay)</li><li>Kilbride, Maelle (Vellmore University)</li><li>Kingsmill, Tarek (Corrin Institute)</li><li>Knowlton, Esme (Ashcombe)</li><li>Lamberth, Pax (Tessaly)</li><li>Larkby, Odette (Lowmarsh University)</li><li>Lassiter, Hume (Northgate University)</li><li>Leaming, Carys (Eastfold University)</li><li>Ledbury, Wynn (Harlow Bay)</li><li>Lindell, Saoirse (Tessaly)</li><li>Lockyer, Bede (Corrin Institute)</li><li>Loveridge, Annika (Ravensmere University)</li><li>Lyndhurst, Kit (Eastfold University)</li>
    </ul>
    <ul class="collab-list right">
      <li>Mabberley, Ione (Northgate University)</li><li>Macklin, Rudi (Tessaly)</li><li>Maddox-Hay, Seren (Eastfold University)</li><li>Malvern, Idris (Ravensmere University)</li><li>Marchbank, Tove (Vellmore University)</li><li>Marwood, Anselm (Tessaly)</li><li>Maybury, Petra (Eastfold University)</li><li>Meldrum, Lachie (Northgate University)</li><li>Merrifield, Zara (Harlow Bay)</li><li>Millbank, Oriel (Northgate University)</li><li>Moffatt, Cosmo (Northgate University)</li><li>Morland, Liesel (Harlow Bay)</li><li>Mowbray, Tiago (Eastfold University)</li><li>Nance, Freya (Harlow Bay)</li><li>Netherby, Ansel (Ravensmere University)</li><li>Newbold, Rhian (Ravensmere University)</li><li>Norcott, Evander (Eastfold University)</li><li>Nyland, Gwen (Harlow Bay)</li><li>Oakden, Marius (Harlow Bay)</li><li>Orme, Tilda (Ashcombe)</li><li>Osterley, Faisal (Corrin Institute)</li><li>Padgett, Romilly (Ashcombe)</li><li>Palliser, Jasper (Northgate University)</li><li>Parnell-Wood, Elke (Kestrel Learning)</li><li>Pendry, Osric (Tessaly)</li><li>Penwarden, Nadia (Northgate University)</li><li>Pickering-Low, Hugo (Ashcombe)</li><li>Pilbeam, Fleur (Tessaly)</li><li>Prewitt, Aziz (Tessaly)</li><li>Pryor, Linnea (Harlow Bay)</li><li>Quarrell, Dex (Lowmarsh University)</li><li>Radley, Maren (Harlow Bay)</li><li>Ramsbury, Eamon (Northgate University)</li><li>Redfern, Sylva (Harlow Bay)</li><li>Renwick, Tully (Ravensmere University)</li><li>Ridgeway, Acacia (Wyndale University)</li><li>Rockliffe, Jem (Eastfold University)</li><li>Rowntree-Bell, Ilona (Tessaly)</li><li>Rushbrook, Caspian (Vellmore University)</li><li>Salter, Wilhelmina (Northgate University)</li><li>Sandow, Remy (Eastfold University)</li><li>Scarfe, Honor (Tessaly)</li><li>Selwood, Piers (Tessaly)</li><li>Sheringham, Adaeze (Northgate University)</li><li>Shillito, Bryn (Ravensmere University)</li><li>Skelton, Vesna (Northgate University)</li><li>Sowerby, Gideon (Lowmarsh University)</li><li>Stainer, Ottoline (Harlow Bay)</li><li>Stanway, Mordecai (Tessaly)</li><li>Stobart, Liane (Corrin Institute)</li><li>Sutcliffe-Ng, Darcy (Lowmarsh University)</li><li>Swinden, Perrin (Harlow Bay)</li><li>Tabor, Ysella (Ravensmere University)</li><li>Tallis, Conrad (Northgate University)</li><li>Tarrant, Minna (Eastfold University)</li><li>Thackray, Soren (Harlow Bay)</li><li>Thornbury, Elodie (Lowmarsh University)</li><li>Tillotson, Ambrose (Corrin Institute)</li><li>Trelawn, Kasia (Ravensmere University)</li><li>Tunnicliffe, Jude (Eastfold University)</li><li>Tyndall, Roisin (Harlow Bay)</li><li>Upcott, Lazlo (Tessaly)</li><li>Vallance, Greer (Vellmore University)</li><li>Varley, Ashby (Northgate University)</li><li>Venables, Isolde (Corrin Institute)</li><li>Voss-Carden, Milo (Tessaly)</li><li>Wadlow, Cerys (Harlow Bay)</li><li>Walbrook, Emeric (Ravensmere University)</li><li>Warrender, Posy (Eastfold University)</li><li>Weatherby, Alaric (Lowmarsh University)</li><li>Wellbeloved, Nyree (Harlow Bay)</li><li>Westerby, Fabian (Corrin Institute)</li><li>Whitcombe, Lark (Tessaly)</li><li>Wickstead, Orla (Northgate University)</li><li>Wilmott, Stellan (Eastfold University)</li><li>Winsor, Amara (Ravensmere University)</li><li>Woodhatch, Rufus (Harlow Bay)</li><li>Worrall, Celeste (Vellmore University)</li><li>Wrexley, Tamar (Tessaly)</li><li>Yardley, Benedikt (Corrin Institute)</li><li>Yelland, Mireille (Northgate University)</li><li>Youlden, Crispin (Ashcombe)</li><li>Zellner, Hanne (Eastfold University)</li><li>Zouch, Everett (Tessaly)</li>
    </ul>
  </aside>
</main>
</body>
</html>
```